DOVVRANTI Label and bottle design

We have already provided attached an idea concept of a label and bottle shape example, we now require designers to take this basic concept and advance it to the final label design using your own design creativity.
Please see attached the full product brief

```html
<!DOCTYPE html>
<html lang="en">
<head>
<meta charset="utf-8">
<title>DOVVRANTI – INK CLEAR Label</title>
<link href="https://fonts.googleapis.com/css2?family=Montserrat:wght@300;400;500;600;700&family=Poppins:ital,wght@0,800;1,800;1,900&display=swap" rel="stylesheet">
<style>
  :root {
    --backdrop: #e2e2e2;
    --label-black: #141414;
    --brand-yellow: #ffe600;
    --text-yellow: #f3df1c;
    --white: #ffffff;
    --pattern-edge: #1f1f16;
  }
  * { margin: 0; padding: 0; box-sizing: border-box; }
  html, body {
    width: 849px; height: 1200px; overflow: hidden;
    background: var(--backdrop);
    font-family: "Montserrat", sans-serif;
  }
  .label {
    position: absolute; left: 20px; top: 281px;
    width: 809px; height: 638px;
    background: var(--label-black);
    overflow: hidden;
    color: var(--text-yellow);
  }
  .honeycomb-area {
    position: absolute; left: 0; top: 0; width: 410px; height: 638px;
    background: radial-gradient(ellipse at 45% 40%, var(--pattern-edge), var(--label-black) 75%);
  }
  .corner-band { position: absolute; left: 0; top: 0; }

  /* Front panel */
  .brand-name {
    position: absolute; left: 37px; top: 92px; width: 330px;
    font-family: "Poppins", sans-serif; font-weight: 800; font-style: normal;
    font-size: 47px; line-height: 1; color: var(--brand-yellow);
    letter-spacing: 0.5px;
  }
  .tagline {
    position: absolute; left: 38px; top: 203px;
    font-size: 9.6px; font-weight: 500; letter-spacing: 0.3px;
    color: var(--brand-yellow);
  }
  .product-name {
    position: absolute; left: 38px; top: 224px;
    font-family: "Poppins", sans-serif; font-style: italic; font-weight: 900;
    font-size: 52px; line-height: 1.1; letter-spacing: 0.5px;
    color: var(--white);
    border-bottom: 2px solid var(--brand-yellow); padding-right: 4px;
  }
  .product-name .accent { color: var(--brand-yellow); }
  .product-type {
    position: absolute; left: 38px; top: 287px;
    font-size: 18.4px; font-weight: 400; letter-spacing: 0.3px;
    color: var(--brand-yellow);
  }
  .product-claims {
    position: absolute; left: 38px; top: 309px;
    font-size: 9.4px; font-weight: 400; color: var(--white);
    border-bottom: 1px solid var(--brand-yellow); padding-bottom: 1px;
  }
  .ink-badges { position: absolute; left: 38px; top: 342px; display: flex; gap: 28px; }
  .ink-badge { position: relative; width: 90px; height: 90px; }
  .ink-badge svg { position: absolute; inset: 0; }
  .ink-badge span {
    position: absolute; left: 0; right: 0; top: 45px;
    text-align: center; font-weight: 700; font-size: 11px; line-height: 12.5px;
    color: var(--label-black);
  }
  .net-weight {
    position: absolute; left: 37px; top: 560px;
    display: flex; align-items: center; gap: 2px;
    font-family: "Poppins", sans-serif; font-weight: 800; font-size: 22px;
    color: var(--label-black);
  }

  /* Info panel */
  .info-panel { position: absolute; left: 434px; top: 0; width: 345px; }
  .section-head {
    position: absolute; left: 0; width: 345px; height: 18px;
    display: flex; align-items: center;
  }
  .section-head h2 {
    font-family: "Poppins", sans-serif; font-style: italic; font-weight: 800;
    font-size: 15px; line-height: 16px; color: var(--label-black);
    background: var(--brand-yellow); border-radius: 9px;
    padding: 1px 8px 0 6px; white-space: nowrap;
  }
  .section-head::after {
    content: ""; flex: 1; height: 4px; margin-left: -2px;
    border-top: 1.5px solid var(--brand-yellow); border-bottom: 1.5px solid var(--brand-yellow);
  }
  .body-copy {
    position: absolute; left: 0; width: 345px;
    font-size: 10.6px; line-height: 12.8px; font-weight: 400; text-align: justify;
  }
  .body-copy p + p { margin-top: 8px; }
  .body-copy b { font-weight: 700; }
  .steps { list-style: none; }
  .steps li { padding-left: 13px; text-indent: -13px; margin-bottom: 8px; text-align: left; }
  .closing p { text-align: left; }
  .contains { position: absolute; left: 5px; top: 505px; font-size: 7.8px; font-weight: 700; }
  .hazard-icon { position: absolute; left: 6px; top: 525px; }
  .hazard-text {
    position: absolute; left: 56px; top: 520px; width: 289px;
    font-size: 7.2px; line-height: 8.4px; text-align: justify;
  }
  .footer-brand {
    position: absolute; left: 2px; top: 582px;
    font-weight: 700; font-size: 13px; color: var(--brand-yellow);
  }
  .footer-contact {
    position: absolute; left: 86px; top: 577px;
    font-size: 9.4px; line-height: 11px;
  }
  .footer-contact b { font-weight: 700; }
</style>
</head>
<body>
  <main class="label">
    <div class="honeycomb-area" role="img" aria-label="Honeycomb hexagon line pattern in yellow on black"></div>
    <svg class="corner-band" width="809" height="638" aria-hidden="true">
      <polygon points="0,497 364,638 0,638" fill="#ffe600"/>
    </svg>

    <section class="front-panel">
      <div class="brand-name">DOVVRANTI</div>
      <p class="tagline">PROFESSIONAL CLEANING | MAXIMUM PERFORMANCE</p>
      <h1 class="product-name"><span class="accent">INK</span> CLEAR</h1>
      <p class="product-type">ADVANCED ANILOX CLEANING GEL</p>
      <p class="product-claims">NON CAUSTIC | NON TOXIC | NON FLAMMABLE | NON CORROSIVE</p>

      <div class="ink-badges">
        <div class="ink-badge">
          <svg viewBox="0 0 90 90"><polygon points="26,2 64,2 88,26 88,64 64,88 26,88 2,64 2,26" fill="#ffe600" stroke="#141414" stroke-width="2"/><polygon points="27,5 63,5 85,27 85,63 63,85 27,85 5,63 5,27" fill="none" stroke="#141414" stroke-width="1"/><path d="M45 12 C48 22 53 27 53 33 a8 8 0 0 1 -16 0 C37 27 42 22 45 12Z" fill="#141414"/><path d="M41 33 a4 4 0 0 0 3 4" stroke="#ffe600" stroke-width="1.2" fill="none"/></svg>
          <span>UV<br>BASED<br>INKS</span>
        </div>
        <div class="ink-badge">
          <svg viewBox="0 0 90 90"><polygon points="26,2 64,2 88,26 88,64 64,88 26,88 2,64 2,26" fill="#ffe600" stroke="#141414" stroke-width="2"/><polygon points="27,5 63,5 85,27 85,63 63,85 27,85 5,63 5,27" fill="none" stroke="#141414" stroke-width="1"/><path d="M45 12 C48 22 53 27 53 33 a8 8 0 0 1 -16 0 C37 27 42 22 45 12Z" fill="#141414"/><path d="M41 33 a4 4 0 0 0 3 4" stroke="#ffe600" stroke-width="1.2" fill="none"/></svg>
          <span>WATER<br>BASED<br>INKS</span>
        </div>
        <div class="ink-badge">
          <svg viewBox="0 0 90 90"><polygon points="26,2 64,2 88,26 88,64 64,88 26,88 2,64 2,26" fill="#ffe600" stroke="#141414" stroke-width="2"/><polygon points="27,5 63,5 85,27 85,63 63,85 27,85 5,63 5,27" fill="none" stroke="#141414" stroke-width="1"/><path d="M45 12 C48 22 53 27 53 33 a8 8 0 0 1 -16 0 C37 27 42 22 45 12Z" fill="#141414"/><path d="M41 33 a4 4 0 0 0 3 4" stroke="#ffe600" stroke-width="1.2" fill="none"/></svg>
          <span>SOLVENT<br>BASED<br>INKS</span>
        </div>
      </div>

      <div class="net-weight">
        <svg width="20" height="30" viewBox="0 0 20 30" aria-hidden="true"><path d="M10 0 C13 9 19 14 19 20 a9 9 0 0 1 -18 0 C1 14 7 9 10 0Z" fill="#141414"/><path d="M5 20 a5 5 0 0 0 4 5" stroke="#ffe600" stroke-width="1.5" fill="none"/></svg>
        1 KG
      </div>
    </section>

    <section class="info-panel">
      <div class="section-head" style="top:39px"><h2>USES</h2></div>
      <div class="body-copy" style="top:62px">
        <p><b>INK CLEAR</b> is a highly concentrated, powerful cleaning gel formulated to safely remove solvent-based, water-based, and UV inks from anilox rollers. It’s thickened formula clings to surfaces, allowing deep penetration into anilox cells and is safe for use on both ceramic and chrome rollers.</p>
        <p><b>INK CLEAR Gel</b> is also suitable for general pressroom cleaning of machinery, components and floors Additionally, it can be used to remove most varnishes, coatings, and emulsion adhesives.</p>
      </div>

      <div class="section-head" style="top:202px"><h2>DIRECTIONS</h2></div>
      <div class="body-copy" style="top:226px">
        <ol class="steps">
          <li><b>1. Apply:</b> Apply INK CLEAR Gel directly to the surface of the anilox roller using an anilox cleaning pad or brush. Ensure full and even coverage with a thick layer of gel.</li>
          <li><b>2. Dwell Time:</b> Allow the gel to sit for 10–15 minutes.</li>
          <li><b>3. Agitate:</b> Use a anilox cleaning pad or brush to agitate and remove stubborn ink deposits.</li>
          <li><b>4. Rinse Thoroughly:</b> Rinse the roller thoroughly with warm water to remove all residue.</li>
          <li><b>5. Dry:</b> Wipe dry with a clean lint-free cloth making sure the roller is completely dry before returning to production.</li>
        </ol>
        <div class="closing">
          <p><b>INK CLEAR Gel</b> can also be used for general press cleaning (rubber rollers, ink trays, doctor blades, press room floors etc)</p>
          <p style="margin-top:8px"><b>For more information see full product data sheet<br>Caution</b> – pre testing on all surfaces is recommended before use.</p>
        </div>
      </div>

      <div class="section-head" style="top:484px"><h2>HEALTH AND SAFETY</h2></div>
      <p class="contains">Contains - &lt;5% Non-Ionic surfactants</p>
      <svg class="hazard-icon" width="42" height="42" viewBox="0 0 42 42" aria-hidden="true"><polygon points="12,1 30,1 41,12 41,30 30,41 12,41 1,30 1,12" fill="#ffe600"/><rect x="18.5" y="9" width="5" height="16" rx="2" fill="#141414"/><circle cx="21" cy="31" r="3" fill="#141414"/></svg>
      <p class="hazard-text"><b>WARNING Contains:</b> Alcohols, C9-11, ethoxylated. Causes skin irritation. Causes serious eye irritation. Wash hands thoroughly after handling. Wear eye protection. IF IN EYES: Rinse cautiously with water for several minutes. Remove contact lenses, if present and easy to do. Continue rinsing. If eye irritation persists: Get medical advice/attention.</p>

      <div class="footer-brand">DOVVRANTI</div>
      <p class="footer-contact">See SDS for full safety information<br><b>DOVVRANTI LTD</b> 48 Harbour Lane, Leith, EH6 7QT<br>Email: info@dovvranti.co.uk | www.dovvranti.co.uk</p>
    </section>
  </main>
</body>
</html>
```